Calderwell Homes

To produce a business card design for our newly established house building and development company, We have had a logo design done please see attached, our slogan is "building your home sweet home"
Contact Information for Business Card
Adress on card needs to Read - 47 Hollowmere Lane, Kettering, Northamptonshire NN14 3QX. Director name Mark Ellery
Requirements
Must have
- Web adress is www.calderwell-homes.co.uk
- Email address is info@calderwell-homes.co.uk
- phone number 07700 900418

```html
<!DOCTYPE html>
<html lang="en">
<head>
<meta charset="utf-8">
<title>Calderwell Homes — Business Card</title>
<link href="https://fonts.googleapis.com/css2?family=Montserrat:wght@700&family=Roboto+Condensed:wght@400;700&display=swap" rel="stylesheet">
<style>
  :root {
    --page: #a9b3c1;
    --card: #131414;
    --green: #8cc63f;
    --grey: #a7a7a7;
  }
  html, body {
    margin: 0;
    width: 1200px;
    height: 1200px;
    overflow: hidden;
    background: var(--page);
  }
  .card {
    position: absolute;
    background: var(--card);
    font-family: "Roboto Condensed", sans-serif;
    color: var(--grey);
  }
  .card--front { left: 148px; top: 63px; width: 854px; height: 511px; }
  .card--back  { left: 141px; top: 627px; width: 870px; height: 498px; }

  .rule {
    position: absolute;
    height: 3px;
    background: var(--green);
  }
  .card--front .rule { top: 250px; }
  .card--back .rule  { top: 224px; }

  .wordmark {
    position: absolute;
    margin: 0;
    font-family: "Montserrat", sans-serif;
    font-weight: 700;
    color: var(--green);
    text-transform: uppercase;
    white-space: nowrap;
    line-height: 1;
    transform: translateX(-50%);
  }
  .card--front .wordmark { left: 430px; top: 206px; font-size: 33px; }
  .card--back .wordmark  { left: 196px; top: 180px; font-size: 33px; }

  .contact {
    position: absolute;
    right: 82px;
    top: 146px;
    text-align: right;
  }
  .contact__name {
    margin: 0;
    font-weight: 700;
    font-size: 46px;
    line-height: 1;
    letter-spacing: -1px;
    color: var(--grey);
  }
  .contact__name .surname { color: var(--green); }
  .contact__role {
    margin: 2px 0 0;
    font-size: 22px;
    line-height: 1.2;
  }
  .contact__address {
    margin: 26px 0 0;
    font-size: 22px;
    line-height: 29px;
    font-style: normal;
  }
  .contact__lines {
    margin: 30px 0 0;
    font-size: 22px;
    line-height: 28px;
  }
</style>
</head>
<body>
  <section class="card card--front">
    <div class="rule" style="left:0;width:238px"></div>
    <h1 class="wordmark">Calderwell Homes</h1>
    <div class="rule" style="left:622px;right:0"></div>
  </section>

  <section class="card card--back">
    <div class="rule" style="left:0;width:30px"></div>
    <h2 class="wordmark">Calderwell Homes</h2>
    <div class="rule" style="left:362px;width:427px"></div>
    <div class="rule" style="left:813px;right:0"></div>

    <div class="contact">
      <p class="contact__name">Mark <span class="surname">Ellery</span></p>
      <p class="contact__role">Director</p>
      <address class="contact__address">47 Hollowmere Lane, Kettering,<br>Northamptonshire NN14 3QX</address>
      <p class="contact__lines">07700 900418<br>info@calderwell-homes.co.uk<br>www.calderwell-homes.co.uk</p>
    </div>
  </section>
</body>
</html>
```